website design for B&T Electric

A portfolio website for a high end commercial and residential electrical contracting company. The current site bandtelectric.example does not represent the current direction but the images in the gallery give you an idea of the work we do. Current logo will be uploaded shortly but is black text on white background.
Target Market(s)
General Contractors, Residential Home Owners, clients intersted in Quavis home automation.
Industry/Entity Type
Electrician
Coding
Coded - Design and coding required
Number of Pages Required
2 page
Font styles to use
Sans Serif
Colors
Designer to choose colors to be used in the design.
Requirements
Must have
- Portfolio section highlighting different service areas and products (Quavis Dwellsync, etc)

```html
<!DOCTYPE html>
<html lang="en">
<head>
<meta charset="utf-8">
<title>B&amp;T Electric</title>
<link href="https://fonts.googleapis.com/css2?family=Questrial&family=Arimo:wght@400;700&display=swap" rel="stylesheet">
<style>
:root{
  --ink:#111;
  --black:#000;
  --charcoal:#3a3a3a;
  --nav:#6b6b6b;
  --nav-active:#111;
  --footer:#3b3b3b;
  --footer-base:#2a2a2a;
  --text:#555;
  --white:#fff;
  --caption:rgba(30,30,35,.82);
  --rule:#dcdcdc;
}
*{box-sizing:border-box;margin:0;padding:0}
html,body{width:1200px;height:2344px;overflow:hidden;background:var(--white)}
body{font-family:"Arimo",sans-serif;color:var(--text);position:relative}
.abs{position:absolute}

/* header */
.site-header{position:absolute;left:0;top:0;width:1200px;height:105px;background:var(--white)}
.brand{position:absolute;left:78px;top:24px;font-family:"Questrial",sans-serif;font-size:50px;color:var(--ink);letter-spacing:1px}
.contact-item{position:absolute;top:28px;display:flex;gap:14px;align-items:center}
.contact-item .label{font-size:16px;color:#888;text-transform:uppercase;line-height:1}
.contact-item .value{font-size:21px;color:var(--ink);line-height:1.2;white-space:nowrap}

/* nav */
.main-nav{position:absolute;left:0;top:105px;width:1200px;height:62px;background:var(--nav)}
.main-nav ul{list-style:none;display:flex;margin-left:78px;height:62px}
.main-nav li{font-size:15px;color:var(--white);padding:0 23px;line-height:62px;letter-spacing:.3px}
.main-nav li.active{background:var(--nav-active)}

/* hero */
.hero{position:absolute;left:0;top:167px;width:1200px;height:468px;overflow:hidden;
  background:radial-gradient(circle at 75% 35%,rgba(255,230,150,.55),transparent 25%),
  radial-gradient(circle at 20% 45%,rgba(255,240,180,.45),transparent 18%),
  radial-gradient(ellipse at 50% 90%,#6b2e1c,transparent 55%),
  linear-gradient(180deg,#0f1a0c 0%,#2f4a1e 40%,#3b2a16 100%)}
.hero h1{position:absolute;top:134px;width:100%;text-align:center;font-family:"Questrial",sans-serif;font-weight:400;font-size:80px;color:var(--white)}
.btn-dark{position:absolute;left:497px;top:265px;width:206px;height:52px;background:#000;border:2px solid var(--white);border-radius:4px;color:var(--white);font-size:17px;text-align:center;line-height:48px}
.hero-arrow{position:absolute;top:215px;width:40px;height:40px;background:rgba(120,120,120,.75);color:var(--white);font-size:22px;text-align:center;line-height:38px}

/* work */
.work{position:absolute;top:635px;width:600px;height:260px;color:var(--white)}
.work.residential{left:0;background:var(--black)}
.work.commercial{left:600px;background:var(--charcoal)}
.work h2{font-family:"Questrial",sans-serif;font-weight:400;font-size:37px;position:absolute;top:38px}
.work p{font-size:16px;line-height:24px;position:absolute;top:92px;width:320px}
.btn-outline{position:absolute;top:156px;width:166px;height:52px;border:1.5px solid var(--white);border-radius:4px;text-align:center;line-height:50px;font-size:16px}
.work-illustration{position:absolute;top:70px;width:126px;height:126px;background:linear-gradient(180deg,rgba(255,255,255,.16),rgba(255,255,255,.06))}

/* about */
.section-title{position:absolute;width:1200px;text-align:center;font-family:"Questrial",sans-serif;font-weight:400;font-size:40px;color:var(--ink)}
.about-text{position:absolute;left:120px;top:1006px;width:960px;text-align:center;font-size:15.5px;line-height:25px;color:#555}
.tile{position:absolute;top:1114px;width:250px;height:188px}
.tile-caption{position:absolute;left:0;bottom:0;width:100%;height:62px;background:rgba(60,60,60,.8);color:var(--white);font-family:"Questrial",sans-serif;font-size:21px;line-height:26px;text-align:center;display:flex;align-items:center;justify-content:center}
.divider{position:absolute;left:78px;top:1353px;width:1044px;height:1px;background:var(--rule)}

/* projects */
.project{position:absolute}
.project-caption{position:absolute;left:0;bottom:0;width:100%;height:72px;background:var(--caption);color:var(--white);padding:12px 22px}
.project-caption strong{display:block;font-family:"Questrial",sans-serif;font-weight:400;font-size:20px;line-height:24px}
.project-caption span{font-size:14px}

/* footer */
.site-footer{position:absolute;left:0;top:2011px;width:1200px;height:248px;background:var(--footer);color:var(--white)}
.footer-col{position:absolute;top:28px}
.footer-col h3{font-family:"Questrial",sans-serif;font-weight:400;font-size:21px;margin-bottom:16px}
.links li{list-style:none;font-size:14px;line-height:31px}
.links li::before{content:"›";margin-right:12px}
.info{display:flex;gap:14px;font-size:14px;line-height:22px;margin-bottom:14px}
.info svg{flex:none;margin-top:3px}
.latest-item{display:flex;gap:16px;margin-bottom:18px}
.latest-item .thumb{width:50px;height:50px;flex:none}
.latest-item b{display:block;font-size:14px;line-height:19px}
.latest-item small{font-size:11px}
.slider-btn{display:inline-block;width:20px;height:20px;border:1px solid #ccc;background:var(--white);color:#222;text-align:center;line-height:18px;font-size:14px}
.avatar{width:64px;height:64px;border-radius:50%;background:linear-gradient(135deg,#a9a9a9,#5a5a5a);border:3px solid var(--white)}
.bottom-bar{position:absolute;left:0;top:2259px;width:1200px;height:85px;background:var(--footer-base);color:#ccc}
.social{position:absolute;top:22px;width:42px;height:42px;background:#4a4a4a}
.social.first{background:#3b5998}
.subscribe{position:absolute;left:790px;top:22px;width:332px;height:42px;background:#efefef;display:flex;align-items:center}
.subscribe span{font-size:13px;color:#999;font-style:italic;margin-left:12px;flex:1}
.subscribe b{background:var(--white);color:#111;font-size:14px;height:42px;line-height:42px;padding:0 12px;font-weight:400}
</style>
</head>
<body>

<header class="site-header">
  <div class="brand">B&amp;T Electric</div>
  <div class="contact-item" style="left:566px">
    <svg width="22" height="40" viewBox="0 0 22 40" fill="none" stroke="#111" stroke-width="2"><rect x="2" y="2" width="18" height="36" rx="3"/><line x1="2" y1="8" x2="20" y2="8"/><line x1="2" y1="31" x2="20" y2="31"/></svg>
    <div><div class="label">Call us on</div><div class="value">(208) 555-0147</div></div>
  </div>
  <div class="contact-item" style="left:778px">
    <svg width="44" height="36" viewBox="0 0 44 36" fill="none" stroke="#111" stroke-width="2"><path d="M4 4h24v14H14l-6 6v-6H4z"/><path d="M30 12h10v14h-4v5l-5-5H18v-6"/></svg>
    <div><div class="label">Want to talk</div><div class="value">dwebb@bandtelectric.example</div></div>
  </div>
</header>

<nav class="main-nav">
  <ul>
    <li class="active">HOME</li><li>ABOUT</li><li>SERVICES</li><li>PRODUCTS</li><li>PROJECTS</li><li>GALLERY</li><li>CONTACT</li>
  </ul>
</nav>

<section class="hero" role="img" aria-label="Night photo of a wooden boardwalk lined with glowing lamp posts among palm trees">
  <div class="hero-arrow" style="left:0">«</div>
  <div class="hero-arrow" style="right:0">»</div>
  <h1>Walk the Way</h1>
  <div class="btn-dark">VIEW PORTFOLIO</div>
</section>

<section class="work residential">
  <h2 style="left:80px">RESIDENTIAL WORK</h2>
  <p style="left:80px">Lorem Ipsum is simply dummy text of the printing and typesetting industry.</p>
  <div class="btn-outline" style="left:78px">GET STARTED</div>
  <div class="work-illustration" style="left:432px" role="img" aria-label="Line illustration of a modern house"></div>
</section>

<section class="work commercial">
  <div class="work-illustration" style="left:42px" role="img" aria-label="Line illustration of office buildings"></div>
  <h2 style="right:80px">COMMERCIAL WORK</h2>
  <p style="right:80px;text-align:right">Lorem Ipsum is simply dummy text of the printing and typesetting industry.</p>
  <div class="btn-outline" style="right:78px">GET STARTED</div>
</section>

<h2 class="section-title" style="top:945px">About Us</h2>
<p class="about-text">B &amp; T Electric is a full service electrical contracting shop. We offer commercial, residential, light industrial, and agricultural services. We're Quavis Dwellsync and Quavis Motorized Shades certified, as well as an authorized Voltmere generator dealer. We've served the Wood River and South Central Idaho area for over 18 years.</p>

<div class="tile" style="left:78px;background:linear-gradient(90deg,#b9a98f,#e5e2dc 50%,#cfc7b8)" role="img" aria-label="Photo of a wall-mounted lighting keypad">
  <div class="tile-caption">QUAVIS<br>DWELLSYNC</div></div>
<div class="tile" style="left:342px;background:linear-gradient(160deg,#9aa0a8,#e8e8ea 55%,#c9c2c2)" role="img" aria-label="Photo of an office with motorized window shades">
  <div class="tile-caption">QUAVIS GLIDELINE QED<br>MOTORIZED SHADES</div></div>
<div class="tile" style="left:606px;background:radial-gradient(circle at 40% 40%,#6a6a6a,#1e1e1e 50%,#e9e9e9 80%)" role="img" aria-label="Photo of LED spotlight bulbs">
  <div class="tile-caption">LED LIGHTING</div></div>
<div class="tile" style="left:870px;background:linear-gradient(150deg,#6e5a48,#e6e6e6 50%,#8a8070)" role="img" aria-label="Photo of a standby generator beside a house">
  <div class="tile-caption">EMERGENCY<br>GENERATORS</div></div>

<div class="divider"></div>

<h2 class="section-title" style="top:1404px">Latest Projects</h2>

<div class="project" style="left:78px;top:1480px;width:333px;height:228px;background:radial-gradient(ellipse at 50% 55%,#d89a45,#5b2a14 55%,#13204a)" role="img" aria-label="Photo of a lit theatre auditorium">
  <div class="project-caption"><strong>Lorem Ipsum is simply</strong><span>Lorem Ipsum is simply dummy text of</span></div></div>
<div class="project" style="left:433px;top:1480px;width:334px;height:476px;background:radial-gradient(circle at 30% 25%,rgba(255,235,170,.5),transparent 25%),linear-gradient(180deg,#0e160c,#2e3f1c 45%,#5a2a18)" role="img" aria-label="Night photo of a lamp-lit wooden boardwalk">
  <div class="project-caption"><strong>Lorem Ipsum is simply</strong><span>Lorem Ipsum is simply dummy text of</span></div></div>
<div class="project" style="left:789px;top:1480px;width:333px;height:228px;background:linear-gradient(180deg,#2a6ae0,#8fb5f2 50%,#1f3fa8)" role="img" aria-label="Photo of a blue-lit modern parking garage">
  <div class="project-caption"><strong>Lorem Ipsum is simply</strong><span>Lorem Ipsum is simply dummy text of</span></div></div>
<div class="project" style="left:78px;top:1728px;width:333px;height:228px;background:linear-gradient(180deg,#6c7f9a,#a7a7ad 40%,#7a4a36 75%,#2c3340)" role="img" aria-label="Photo of lit apartment buildings at dusk">
  <div class="project-caption"><strong>Lorem Ipsum is simply</strong><span>Lorem Ipsum is simply dummy text of</span></div></div>
<div class="project" style="left:789px;top:1728px;width:333px;height:228px;background:linear-gradient(180deg,#e9e2d6,#cbb79a 60%,#8b6b4a)" role="img" aria-label="Photo of a living room with recessed ceiling lighting">
  <div class="project-caption"><strong>Lorem Ipsum is simply</strong><span>Lorem Ipsum is simply dummy text of</span></div></div>

<footer class="site-footer">
  <div class="footer-col" style="left:81px">
    <h3>Useful Links</h3>
    <ul class="links"><li>Home</li><li>Blog</li><li>Privacy Policy</li><li>Terms of Use</li><li>Contact Us</li></ul>
  </div>
  <div class="footer-col" style="left:345px;width:240px">
    <h3>Contact Info</h3>
    <div class="info"><svg width="18" height="24" viewBox="0 0 18 24"><path d="M9 0a9 9 0 0 1 9 9c0 6-9 15-9 15S0 15 0 9a9 9 0 0 1 9-9z" fill="#fff"/><circle cx="9" cy="9" r="3.5" fill="#3b3b3b"/></svg><span>215 Alder Lane, PO Box<br>4120, Millbrook, ID 83399</span></div>
    <div class="info"><svg width="18" height="18" viewBox="0 0 18 18"><path d="M4 1l3 4-2 2c1 2 3 4 6 6l2-2 4 3-2 3C8 17 1 10 1 3z" fill="#fff"/></svg><span>(208) 555-0147</span></div>
    <div class="info"><svg width="18" height="14" viewBox="0 0 18 14" fill="none" stroke="#fff" stroke-width="1.6"><rect x="1" y="1" width="16" height="12"/><path d="M1 1l8 7 8-7"/></svg><span>dwebb@bandtelectric.example<br>tmorris@bandtelectric.example</span></div>
  </div>
  <div class="footer-col" style="left:609px;width:240px">
    <h3>Latest Project</h3>
    <div class="latest-item"><div class="thumb" style="background:linear-gradient(135deg,#c89a78,#6a4a3a)" role="img" aria-label="Project thumbnail"></div><div><b>Lorem Ipsum is simply<br>dummy text of</b><small>12.06.2014</small></div></div>
    <div class="latest-item"><div class="thumb" style="background:linear-gradient(135deg,#e6dccb,#8c7556)" role="img" aria-label="Project thumbnail"></div><div><b>Lorem Ipsum is simply<br>dummy text of</b><small>12.06.2014</small></div></div>
  </div>
  <div class="footer-col" style="left:873px;width:250px">
    <h3>Testimonials</h3>
    <div class="abs" style="left:202px;top:2px"><span class="slider-btn">‹</span> <span class="slider-btn">›</span></div>
    <div style="display:flex;gap:14px;align-items:center;margin-top:-4px">
      <div class="avatar" role="img" aria-label="Portrait of the reviewer"></div>
      <div><div style="font-size:15px">Mark Halden</div><div style="font-size:13px;font-style:italic">CEO</div></div>
    </div>
    <p style="font-size:13px;line-height:20px;margin-top:8px">"Lorem Ipsum is simply dummy text of the printing and typesetting industry. Lorem Ipsum has been the industry."</p>
  </div>
</footer>

<div class="bottom-bar">
  <div class="abs" style="left:80px;top:34px;font-size:13px">© B&amp;T Electric - 2017. All Rights Reserved.</div>
  <div class="social first" style="left:503px" role="img" aria-label="Social link"></div>
  <div class="social" style="left:553px" role="img" aria-label="Social link"></div>
  <div class="social" style="left:603px" role="img" aria-label="Social link"></div>
  <div class="social" style="left:653px" role="img" aria-label="Social link"></div>
  <div class="subscribe">
    <svg style="margin-left:16px" width="22" height="16" viewBox="0 0 22 16"><rect width="22" height="16" fill="#111"/><path d="M1 1l10 8 10-8" fill="none" stroke="#efefef" stroke-width="1.5"/></svg>
    <span>Enter E-Mail Id</span><b>SUBSCRIBE</b>
  </div>
</div>

</body>
</html>
```